Homepage web design

I need a homepage design that will be easy to build into a default Word Press theme. Basically, header, navigation, body with sidebar, and footer.

This website is for a small commercial real estate firm in the Washington DC, Maryland and Virginia market.

THIS IS NOT A HOUSING/RESIDENTIAL WEBSITE. PLEASE DO NOT ADD ANY PROPERTY SEARCH FUNCTIONALITY.

Target Market(s)

People looking for basic information about the team and services provided.

Industry/Entity Type

Real Estate

Requirements
Must have
• Professional look. Clean design.

```html
<!DOCTYPE html>
<html lang="en">
<head>
<meta charset="utf-8">
<title>KRB — Keystone Realty Brokerage</title>
<link href="https://fonts.googleapis.com/css2?family=Lato:wght@400;700&family=Noto+Serif&display=swap" rel="stylesheet">
<style>
:root{
  --green:#0b8a4f;
  --green-dark:#06693a;
  --green-deep:#045a31;
  --green-text:#0b7a45;
  --ink:#333333;
  --muted:#555555;
  --grey:#888888;
  --header-top:#ffffff;
  --header-bottom:#e9e9e9;
  --social-a:#2c4a8c;
  --social-b:#1f6fb0;
  --social-c:#2aa3e0;
}
*{margin:0;padding:0;box-sizing:border-box}
html,body{width:1200px;height:790px;overflow:hidden}
body{position:relative;font-family:'Lato',sans-serif;color:var(--ink);background:#fff}
.site-header{position:absolute;left:0;top:0;width:1200px;height:104px;background:linear-gradient(var(--header-top),var(--header-bottom))}
.header-rule{position:absolute;left:0;top:99px;width:1200px;height:5px;background:var(--green)}
.brand{position:absolute;left:192px;top:30px;display:flex;align-items:center;gap:8px}
.brand-mark{width:14px;height:14px;background:var(--green)}
.brand-name{font-size:48px;font-weight:700;color:var(--green);line-height:1;letter-spacing:1px}
.header-contact{position:absolute;left:700px;top:20px;display:flex;align-items:center;height:26px}
.header-phone{font-size:20px;color:var(--ink);margin-left:12px}
.header-divider{width:1px;height:20px;background:#ccc;margin:0 10px}
.follow-label{font-size:13px;color:var(--grey);margin-right:8px}
.social{display:flex;gap:5px}
.social span{width:19px;height:19px;border-radius:3px;display:block}
.social span:nth-child(1){background:var(--social-a)}
.social span:nth-child(2){background:var(--social-b)}
.social span:nth-child(3){background:var(--social-c)}
.main-nav{position:absolute;left:627px;top:76px;display:flex;height:23px}
.main-nav a{font-size:15px;font-weight:700;color:var(--ink);text-decoration:none;padding:0 13px;line-height:24px;border-right:3px solid #fff}
.main-nav a:last-child{border-right:none}
.main-nav a.current{background:var(--green);color:#fff;width:71px;text-align:center;padding:0}
.hero{position:absolute;left:0;top:104px;width:1200px;height:569px;background:linear-gradient(100deg,#8e8e8e 0%,#c9c6c0 25%,#ddd9d2 45%,#e9eef2 70%,#dcdfe2 100%)}
.welcome-panel{position:absolute;left:199px;top:221px;width:802px;height:348px;background:rgba(255,255,255,.88)}
.ribbon{position:absolute;left:190px;top:233px;width:820px;height:53px}
.ribbon-title{position:absolute;left:205px;top:240px;font-family:'Noto Serif',serif;font-size:26px;color:#fff;letter-spacing:.5px}
.intro{position:absolute;left:226px;top:300px;width:750px;font-size:12.5px;line-height:19.5px;color:var(--ink)}
.read-more{position:absolute;left:227px;top:391px;width:72px;height:20px;background:var(--green);border:1px solid var(--green-deep);border-radius:2px;color:#fff;font-size:11px;line-height:18px;padding-left:6px;box-shadow:0 0 0 1px #fff}
.help-title{position:absolute;left:228px;top:432px;font-size:22px;color:var(--green-text)}
.help-col{position:absolute;top:473px}
.help-col h3{font-size:15px;font-weight:400;color:var(--ink);display:flex;align-items:center;gap:7px;height:20px}
.help-col h3 strong{color:var(--green-text);font-weight:700}
.help-col p{font-size:12px;line-height:16px;color:var(--muted);margin-top:6px}
.help-col .social{margin-top:4px;margin-left:3px}
.col-email{left:228px;width:200px}
.col-call{left:461px;width:170px}
.col-follow{left:660px;width:170px}
.col-sep{position:absolute;top:470px;width:2px;height:85px;background:linear-gradient(rgba(0,0,0,0),rgba(0,0,0,.12),rgba(0,0,0,0))}
.site-footer{position:absolute;left:0;top:673px;width:1200px;height:117px;background:var(--green);color:#fff;text-align:center}
.footer-nav{font-size:11px;line-height:16px;padding-top:15px}
.footer-nav a{color:#fff;text-decoration:none}
.footer-rule{position:absolute;left:0;top:44px;width:1200px;height:1px;background:rgba(255,255,255,.15)}
.footer-contact{position:absolute;top:61px;left:0;width:1200px;display:flex;justify-content:center;align-items:center;gap:22px;font-size:13px;font-weight:700}
.footer-contact span{display:flex;align-items:center;gap:8px}
.copyright{position:absolute;top:87px;width:1200px;font-size:11px}
</style>
</head>
<body>
<header class="site-header">
  <div class="brand"><span class="brand-mark"></span><span class="brand-name">KRB</span></div>
  <div class="header-contact">
    <svg width="21" height="15" viewBox="0 0 21 15"><path d="M1 6 Q1 1 10.5 1 Q20 1 20 6 L15 6 L14 3.5 L7 3.5 L6 6 Z" fill="#0b8a4f"/><rect x="3" y="7" width="15" height="8" rx="2" fill="#0b8a4f"/><circle cx="10.5" cy="11" r="2.3" fill="#fff"/></svg>
    <span class="header-phone">000-000-1234</span>
    <span class="header-divider"></span>
    <span class="follow-label">Follow Us</span>
    <span class="social"><span></span><span></span><span></span></span>
  </div>
  <nav class="main-nav">
    <a class="current" href="#">Home</a>
    <a href="#">About KRB</a>
    <a href="#">Properties</a>
    <a href="#">Contact Us</a>
  </nav>
  <div class="header-rule"></div>
</header>

<section class="hero" role="img" aria-label="Photo of a broker meeting clients across a desk in a bright office with building models"></section>

<div class="welcome-panel"></div>
<svg class="ribbon" viewBox="0 0 820 53">
  <defs><linearGradient id="ribbonFill" x1="0" y1="0" x2="0" y2="1"><stop offset="0" stop-color="#0d9655"/><stop offset="1" stop-color="#06703d"/></linearGradient></defs>
  <polygon points="0,8 9,0 9,53 0,45" fill="#045a31"/>
  <polygon points="820,8 811,0 811,53 820,45" fill="#045a31"/>
  <rect x="0" y="0" width="820" height="45" transform="translate(0,4)" fill="url(#ribbonFill)"/>
</svg>
<h1 class="ribbon-title">Welcome to KRB</h1>
<p class="intro">Lorem ipsum dolor sit amet, consectetur adipisicing elit, sed do eiusmod tempor incididunt ut labore et dolore magna aliqua. Ut enim ad minim veniam, quis nostrud exercitation ullamco laboris nisi ut aliquip ex ea commodo consequat. Duis aute irure dolor in reprehenderit in voluptate velit esse cillum dolore eu fugiat nulla pariatur. Excepteur sint occaecat cupidatat non proident, sunt in culpa qui officia deserunt mollit anim id est laborum.</p>
<a class="read-more">Read More ›</a>

<h2 class="help-title">Questions? We're here to help</h2>
<div class="help-col col-email">
  <h3><svg width="24" height="14" viewBox="0 0 24 14"><rect width="24" height="14" fill="#0b8a4f"/><path d="M1 1 L12 8 L23 1" stroke="#fff" stroke-width="1.5" fill="none"/></svg><span><strong>Send</strong> Email</span></h3>
  <p>Get prompt, friendly replies to your enquiries and requests</p>
</div>
<div class="col-sep" style="left:434px"></div>
<div class="help-col col-call">
  <h3><svg width="14" height="14" viewBox="0 0 14 14"><path d="M3 0 L5.5 3.5 L4 5 Q5.5 8.5 9 10 L10.5 8.5 L14 11 L12 14 Q2 12 0 2 Z" fill="#0b8a4f"/></svg><span><strong>Call</strong> Us</span></h3>
  <p>Toll free numbers available<br>9 AM – 5 PM GMT, Mon - Fri</p>
</div>
<div class="col-sep" style="left:633px"></div>
<div class="help-col col-follow">
  <h3><svg width="13" height="13" viewBox="0 0 13 13"><circle cx="6.5" cy="6.5" r="5.5" stroke="#0b8a4f" stroke-width="1.6" fill="none"/><circle cx="6.5" cy="6.5" r="2" fill="#0b8a4f"/></svg><span><strong>Follow</strong> Us</span></h3>
  <p>We’re also available on</p>
  <span class="social"><span></span><span></span><span></span></span>
</div>

<footer class="site-footer">
  <nav class="footer-nav"><a href="#">Home</a> | <a href="#">About KRB</a> | <a href="#">Properties</a> | <a href="#">Contact Us</a></nav>
  <div class="footer-rule"></div>
  <div class="footer-contact">
    <span><svg width="9" height="13" viewBox="0 0 9 13"><path d="M4.5 13 L1 6.5 A4 4 0 1 1 8 6.5 Z" fill="#fff"/><circle cx="4.5" cy="4.5" r="1.5" fill="#0b8a4f"/></svg>2240 Linden Street NW, Washington, DC 20010</span>
    <span style="margin-left:6px"><svg width="21" height="15" viewBox="0 0 21 15"><path d="M1 6 Q1 1 10.5 1 Q20 1 20 6 L15 6 L14 3.5 L7 3.5 L6 6 Z" fill="#fff"/><rect x="3" y="7" width="15" height="8" rx="2" fill="#fff"/><circle cx="10.5" cy="11" r="2.3" fill="#0b8a4f"/></svg>000-000-123</span>
    <span><svg width="22" height="13" viewBox="0 0 22 13"><rect width="22" height="13" fill="#fff"/><path d="M1 1 L11 7.5 L21 1" stroke="#0b8a4f" stroke-width="1.4" fill="none"/></svg>info@krbrealty.com</span>
  </div>
  <p class="copyright">Copyright © 2013 www.krbrealty.com, All Rights Reserved.</p>
</footer>
</body>
</html>
```